Psychotherapist's business card

I need a business card design for a psychotherapist. I expect business card to have "light" design. By this I mean that it can somehow translate easiness, serenity. Maybe pastel colours can help you here. I have attached some pictures from Greece. Perhaps they can inspire you to combine colours and to achieve that "light" design.
Updates

Pls, don't use any free samples you may find on business card generators. It looks too simple, uncreative and waste of time! READ size and colour requirements! I don't want to see any shapes like rings, triangles etc.

Contact Information for Business Card

Size: 65mmX60mm

Name - Вячеслав Мирошенко

Психолог
+7(916)482-30-67
miroshenko.com

I suppose that thin font can look good but it's up to you

Requirements
Must have
• size requirements
Nice to have
• pastel colours
• thin font
Should not have
• black and dark colours
• lines, free design samples used from other web-sites

```html
<!DOCTYPE html>
<html lang="ru">
<head>
<meta charset="utf-8">
<title>Визитная карточка — Вячеслав Мирошенко, психолог</title>
<link rel="stylesheet" href="https://fonts.googleapis.com/css2?family=Jost:wght@400;600&display=swap">
<style>
  :root {
    --backdrop: #efece7;
    --coral: #f8a596;
    --peach-band: #fdd5a8;
    --accent: #f07f6c;
    --ink: #1b1b1b;
    --ink-soft: #2a2a2a;
  }
  * { box-sizing: border-box; margin: 0; padding: 0; }
  html, body {
    width: 1200px;
    height: 1000px;
    overflow: hidden;
    background: var(--backdrop);
  }
  .canvas {
    position: relative;
    width: 1200px;
    height: 1000px;
  }
  .business-card {
    position: absolute;
    left: 210px;
    top: 140px;
    width: 780px;
    height: 720px;
    background: var(--coral);
    overflow: hidden;
    font-family: "Jost", sans-serif;
  }
  .pattern-field {
    position: absolute;
    left: 0;
    width: 100%;
    background: var(--coral);
  }
  .pattern-field--top { top: 0; height: 258px; }
  .pattern-field--bottom { bottom: 0; height: 232px; }
  .info-band {
    position: absolute;
    left: 0;
    top: 258px;
    width: 100%;
    height: 230px;
    background: var(--peach-band);
    display: flex;
    flex-direction: column;
    align-items: center;
    padding-top: 34px;
  }
  .holder-name {
    font-weight: 600;
    font-size: 36px;
    letter-spacing: 0.3px;
    color: var(--ink);
    line-height: 1.1;
  }
  .holder-role {
    font-weight: 400;
    font-size: 25px;
    color: var(--ink-soft);
    line-height: 1.2;
    margin-top: 2px;
  }
  .divider {
    width: 46px;
    height: 3px;
    background: var(--accent);
    margin: 16px 0 18px;
  }
  .contacts {
    list-style: none;
    display: flex;
    flex-direction: column;
    gap: 8px;
  }
  .contact-item {
    display: flex;
    align-items: center;
    gap: 10px;
    font-size: 24px;
    font-weight: 400;
    color: var(--ink-soft);
    line-height: 1.2;
  }
  .contact-icon {
    width: 18px;
    height: 18px;
    flex: none;
  }
</style>
</head>
<body>
<main class="canvas">
  <article class="business-card">
    <div class="pattern-field pattern-field--top" role="img" aria-label="Мягкий узор из светлых персиковых точек на коралловом фоне"></div>

    <section class="info-band">
      <h1 class="holder-name">Вячеслав Мирошенко</h1>
      <p class="holder-role">Психолог</p>
      <div class="divider"></div>
      <ul class="contacts">
        <li class="contact-item">
          <svg class="contact-icon" viewBox="0 0 24 24" aria-hidden="true">
            <path fill="var(--accent)" d="M6.6 10.8a15.1 15.1 0 0 0 6.6 6.6l2.2-2.2a1 1 0 0 1 1-.25 11.4 11.4 0 0 0 3.6.57 1 1 0 0 1 1 1V20a1 1 0 0 1-1 1A17 17 0 0 1 3 4a1 1 0 0 1 1-1h3.5a1 1 0 0 1 1 1c0 1.25.2 2.45.57 3.6a1 1 0 0 1-.25 1z"/>
          </svg>
          <span>+7(916)482-30-67</span>
        </li>
        <li class="contact-item">
          <svg class="contact-icon" viewBox="0 0 24 24" aria-hidden="true">
            <circle cx="12" cy="12" r="11" fill="var(--accent)"/>
            <path d="M1.5 12h21M12 1.5c3 3 3 18 0 21M12 1.5c-3 3-3 18 0 21M3.5 7h17M3.5 17h17" stroke="var(--peach-band)" stroke-width="1.4" fill="none"/>
          </svg>
          <span>miroshenko.com</span>
        </li>
      </ul>
    </section>

    <div class="pattern-field pattern-field--bottom" role="img" aria-label="Мягкий узор из светлых персиковых точек на коралловом фоне"></div>
  </article>
</main>
</body>
</html>
```